Graphic to communicate emotional connection

Howdy-I need a graphic that describe my financial planning process.The attached is a concept, but please use your own creativity to show how you would display this:- The four circles on the outside (Protect what we have, know where it goes, make it grow, and dignity and independence) are the four major areas of concern- Then, there are three value statements:- The first is the most powerful which is that Clarity leads to Control which allows your Intentions to come through- The second shows that we take our clients from Uncertainty and Confusion, to Confidence and Intention- The third says we create space for you to develop your Purposeful Effort which leads to Your Best Financial Life.I've also attached my logo - please use the colors in my logo and maybe add a soft green as needed.The reader should be able to briefly scan this document and understand that we will connect with them on an emotional level to get their finances in shape.Thanks!-Ned

Target Market(s)

wealthy women, whether independent or married

Industry/Entity Type

Financial Planning

Requirements
Must have
• Please use the colors in my logo plus a soft green as needed
Should not have
• This should not be a busy or hard-to-read graphic. It is meant to convey an that I try to make an emotional connection, at a glance.

```html
<!DOCTYPE html>
<html lang="en">
<head>
<meta charset="utf-8">
<title>Our Aspiration – Halvard Wealth Management</title>
<link rel="stylesheet" href="https://fonts.googleapis.com/css2?family=Tinos:wght@400;700&display=swap">
<style>
  :root{
    --navy:#0d3a7c;
    --navy-deep:#0a2f66;
    --slate:#636466;
    --slate-dark:#555658;
    --green:#05a66b;
    --ring-light:#f4f4f5;
    --ring-dark:#c9c9cc;
    --paper:#ffffff;
    --ink-light:#ffffff;
  }
  html,body{margin:0;padding:0;width:1200px;height:900px;overflow:hidden;background:var(--paper);}
  .aspiration-board{display:block;width:1200px;height:900px;font-family:"Tinos","Times New Roman",serif;}
  .brand-name{fill:var(--navy);font-size:38px;font-weight:400;letter-spacing:0.5px;}
  .brand-sub{fill:var(--navy);font-size:17px;letter-spacing:1px;}
  .title-text{fill:var(--ink-light);font-size:40px;}
  .label{fill:var(--ink-light);text-anchor:middle;}
  .label-corner{font-size:17px;}
  .label-small{font-size:13px;}
  .label-value{font-size:13px;}
  .label-bar{font-size:18px;}
  .label-lead{font-size:13px;}
  .label-to{font-size:20px;}
  .label-leads{font-size:16px;}
  .navy-fill{fill:var(--navy);}
  .slate-fill{fill:var(--slate);}
  .green-fill{fill:var(--green);}
  .ring{fill:url(#ringGrad);}
</style>
</head>
<body>
<svg class="aspiration-board" viewBox="0 0 1200 900" xmlns="http://www.w3.org/2000/svg">
  <defs>
    <linearGradient id="ringGrad" x1="0" y1="0" x2="0" y2="1">
      <stop offset="0" stop-color="#f7f7f8"/>
      <stop offset="1" stop-color="#d2d2d5"/>
    </linearGradient>
    <linearGradient id="navyGrad" x1="0" y1="0" x2="0" y2="1">
      <stop offset="0" stop-color="#5a6fa3"/>
      <stop offset="0.35" stop-color="#0d3a7c"/>
      <stop offset="1" stop-color="#0a3576"/>
    </linearGradient>
    <linearGradient id="slateGrad" x1="0" y1="0" x2="0" y2="1">
      <stop offset="0" stop-color="#9a9b9d"/>
      <stop offset="0.35" stop-color="#646567"/>
      <stop offset="1" stop-color="#5c5d5f"/>
    </linearGradient>
    <linearGradient id="greenGrad" x1="0" y1="0" x2="0" y2="1">
      <stop offset="0" stop-color="#5cc897"/>
      <stop offset="0.35" stop-color="#07a86c"/>
      <stop offset="1" stop-color="#05a066"/>
    </linearGradient>
    <linearGradient id="bandGrad" x1="0" y1="0" x2="0" y2="1">
      <stop offset="0" stop-color="#123f80"/>
      <stop offset="1" stop-color="#0a3170"/>
    </linearGradient>
  </defs>

  <!-- Brand -->
  <g class="brand">
    <rect x="70" y="52" width="56" height="56" class="navy-fill"/>
    <text class="brand-name" x="140" y="86">HALVARD WEALTH</text>
    <text class="brand-sub" x="140" y="112">MANAGEMENT, LLC</text>
  </g>

  <!-- Title banner -->
  <g class="title-banner">
    <polygon points="965,112 1200,112 1200,128 980,128" fill="#6b6c6e"/>
    <path d="M737,44 L1200,44 L1200,112 L800,112 Q790,112 782,104 Z" fill="url(#bandGrad)"/>
    <text class="title-text" x="1140" y="95" text-anchor="end">OUR ASPIRATION</text>
  </g>

  <!-- Corner concerns -->
  <g class="concern concern-protect">
    <polygon points="205,330 230,374 175,360" class="ring"/>
    <circle cx="147" cy="287" r="85" class="ring"/>
    <circle cx="147" cy="287" r="63" fill="#8a8a8e"/>
    <circle cx="147" cy="287" r="59" fill="url(#navyGrad)"/>
    <text class="label label-corner" x="147" y="269">PROTECT</text>
    <text class="label label-corner" x="147" y="290">WHAT WE</text>
    <text class="label label-corner" x="147" y="311">HAVE</text>
  </g>
  <g class="concern concern-know">
    <polygon points="995,330 970,374 1025,360" class="ring"/>
    <circle cx="1053" cy="287" r="85" class="ring"/>
    <circle cx="1053" cy="287" r="63" fill="#8a8a8e"/>
    <circle cx="1053" cy="287" r="59" fill="url(#navyGrad)"/>
    <text class="label label-corner" x="1053" y="269">KNOW</text>
    <text class="label label-corner" x="1053" y="290">WHERE IT</text>
    <text class="label label-corner" x="1053" y="311">GOES</text>
  </g>
  <g class="concern concern-grow">
    <polygon points="205,676 230,632 175,646" class="ring"/>
    <circle cx="147" cy="719" r="85" class="ring"/>
    <circle cx="147" cy="719" r="63" fill="#8a8a8e"/>
    <circle cx="147" cy="719" r="59" fill="url(#navyGrad)"/>
    <text class="label label-corner" x="147" y="714">MAKE IT</text>
    <text class="label label-corner" x="147" y="735">GROW</text>
  </g>
  <g class="concern concern-dignity">
    <polygon points="995,676 970,632 1025,646" class="ring"/>
    <circle cx="1053" cy="719" r="85" class="ring"/>
    <circle cx="1053" cy="719" r="63" fill="#8a8a8e"/>
    <circle cx="1053" cy="719" r="59" fill="url(#navyGrad)"/>
    <text class="label label-small" x="1053" y="705">DIGNITY</text>
    <text class="label label-small" x="1053" y="721">+</text>
    <text class="label label-small" x="1053" y="737">INDEPENDENCE</text>
  </g>

  <!-- Value chain: clarity → control → intention -->
  <g class="value value-clarity">
    <polygon points="465,248 505,271 465,294" class="ring"/>
    <circle cx="409" cy="271" r="70" class="ring"/>
    <circle cx="409" cy="271" r="53" fill="#8a8a8e"/>
    <circle cx="409" cy="271" r="50" fill="url(#slateGrad)"/>
    <text class="label label-value" x="409" y="276">CLARITY</text>
  </g>
  <g class="value value-control">
    <polygon points="656,248 696,271 656,294" class="ring"/>
    <circle cx="600" cy="271" r="70" class="ring"/>
    <circle cx="600" cy="271" r="53" fill="#8a8a8e"/>
    <circle cx="600" cy="271" r="50" fill="url(#slateGrad)"/>
    <text class="label label-value" x="600" y="276">CONTROL</text>
  </g>
  <g class="value value-intention">
    <circle cx="790" cy="271" r="70" class="ring"/>
    <circle cx="790" cy="271" r="53" fill="#8a8a8e"/>
    <circle cx="790" cy="271" r="50" fill="url(#slateGrad)"/>
    <text class="label label-value" x="790" y="276">INTENTION</text>
  </g>

  <!-- Row 1: from uncertainty to confidence -->
  <g class="journey journey-from">
    <rect x="330" y="402" width="227" height="78" rx="5" class="slate-fill"/>
    <circle cx="326" cy="441" r="50" fill="#b9b9bc"/>
    <circle cx="326" cy="441" r="46" fill="url(#slateGrad)"/>
    <text class="label label-lead" x="326" y="438">WE TAKE</text>
    <text class="label label-lead" x="326" y="455">YOU FROM</text>
    <text class="label label-bar" x="472" y="434">UNCERTANTY</text>
    <text class="label label-bar" x="472" y="458">CONFUSION</text>
  </g>
  <path class="arrow" d="M580,432 H598 V418 L620,441 L598,464 V450 H580 Z" fill="var(--navy)"/>
  <g class="journey journey-to">
    <rect x="697" y="402" width="223" height="78" rx="5" class="green-fill"/>
    <circle cx="693" cy="441" r="50" fill="#cfd3d1"/>
    <circle cx="693" cy="441" r="46" fill="url(#greenGrad)"/>
    <text class="label label-to" x="693" y="448">TO</text>
    <text class="label label-bar" x="835" y="434">CONFIDENCE</text>
    <text class="label label-bar" x="835" y="458">INTENTION</text>
  </g>

  <!-- Row 2: purposeful effort to best financial life -->
  <g class="journey journey-from">
    <rect x="330" y="531" width="227" height="78" rx="5" class="slate-fill"/>
    <circle cx="326" cy="570" r="50" fill="#b9b9bc"/>
    <circle cx="326" cy="570" r="46" fill="url(#slateGrad)"/>
    <text class="label label-lead" x="326" y="548">WE</text>
    <text class="label label-lead" x="326" y="565">CREATE</text>
    <text class="label label-lead" x="326" y="582">SPACE FOR</text>
    <text class="label label-lead" x="326" y="599">YOUR</text>
    <text class="label label-bar" x="472" y="563">PURPOSEFUL</text>
    <text class="label label-bar" x="472" y="587">EFFORT</text>
  </g>
  <path class="arrow" d="M580,561 H598 V547 L620,570 L598,593 V579 H580 Z" fill="var(--navy)"/>
  <g class="journey journey-to">
    <rect x="697" y="531" width="223" height="78" rx="5" class="green-fill"/>
    <circle cx="693" cy="570" r="50" fill="#cfd3d1"/>
    <circle cx="693" cy="570" r="46" fill="url(#greenGrad)"/>
    <text class="label label-leads" x="693" y="555">WHICH</text>
    <text class="label label-leads" x="693" y="576">LEADS</text>
    <text class="label label-leads" x="693" y="597">TO</text>
    <text class="label label-bar" x="835" y="563">YOUR BEST</text>
    <text class="label label-bar" x="835" y="587">FINANCIAL LIFE</text>
  </g>

  <!-- Footer band -->
  <rect class="footer-band" x="0" y="872" width="1200" height="28" fill="url(#bandGrad)"/>
</svg>
</body>
</html>
```